Web design concept for a IT recruitment agency.

Our website addresses two different target groups:
- Customers (companies) wanting to hire new IT talent
- It talent to find a new JOB

We a looking for a visual design concept that either addresses both target groups in one of the following options:
a. target both groups in 1 single splash page.
b. target both groups in 2 different pages one for both groups
c. or any creative third concept you can come up with

Requirements, we want one overall visual concept, that both target groups can relate to.

Trigger words what we want to express:
- passion / drive
- knowhow
- involvement
- professional/yet playful
- engagement

Background, company culture:
We are a recruitment agency with over 15 years of experience, we have no hard-sale culture.
But we emphasize on long term relationships, showing real interest in people and their needs.

Design requirements:
Use logo
Flat contemporary design

Target Market(s)

Industry/Entity Type

Hire

Number of Pages Required

2 page

Requirements
Must have
• We a looking for a visual design concept that either addresses both target groups

```html
<!DOCTYPE html>
<html lang="en">
<head>
<meta charset="utf-8">
<title>Brightvale – IT Recruitment Specialists</title>
<link rel="stylesheet" href="https://fonts.googleapis.com/css2?family=Roboto:ital,wght@0,300;0,400;0,500;0,700;1,400&display=swap">
<style>
  :root {
    --blue: #00aeef;
    --blue-deep: #1a8fd0;
    --link: #1ea3e6;
    --charcoal: #454344;
    --navy: #2e3d5e;
    --text: #3d4a66;
    --grey-band: #ededed;
    --rule: #cfcfcf;
    --white: #ffffff;
  }
  * { box-sizing: border-box; margin: 0; padding: 0; }
  html, body { width: 1015px; height: 1200px; overflow: hidden; background: var(--white); }
  body { font-family: 'Roboto', sans-serif; color: var(--text); position: relative; }
  .abs { position: absolute; }
  a { text-decoration: none; color: inherit; }

  /* top navigation */
  .top-nav { left: 0; top: 11px; width: 1015px; height: 29px; background: var(--charcoal); }
  .top-nav a { position: absolute; top: 0; line-height: 29px; font-size: 9px; font-weight: 500; color: var(--link); }
  .brand-tab { left: 480px; top: 6px; width: 68px; height: 68px; border-radius: 50%; background: var(--white); }
  .brand { left: 407px; top: 52px; width: 214px; text-align: center; font-size: 26px; font-weight: 400; color: var(--charcoal); line-height: 30px; }
  .brand-dot { left: 498px; top: 20px; width: 32px; height: 32px; border-radius: 50%; background: var(--blue); }

  .social-top span { position: absolute; top: 70px; width: 10px; height: 10px; border-radius: 50%; background: #b9b9b9; }
  .phone { left: 724px; top: 66px; display: flex; align-items: center; gap: 6px; font-size: 13px; color: var(--link); }
  .phone b { font-weight: 400; color: var(--blue-deep); }

  /* hero */
  .hero { left: 115px; top: 110px; width: 785px; height: 242px; }
  .hero-art { position: absolute; left: 0; top: 0; }
  .hero-title { left: 55px; top: 70px; font-size: 32px; font-weight: 300; color: var(--white); line-height: 36px; white-space: nowrap; }
  .hero-sub { left: 55px; top: 109px; font-size: 19px; font-weight: 700; color: var(--white); line-height: 22px; }
  .btn { display: flex; align-items: center; justify-content: space-between; border-radius: 3px; color: var(--white); font-size: 10px; padding: 0 15px; white-space: nowrap; }
  .btn svg { flex: none; }
  .btn-hero { left: 56px; top: 154px; width: 219px; height: 34px; background: var(--charcoal); font-size: 11px; padding: 0 16px 0 18px; }

  .intro { left: 187px; top: 388px; width: 641px; text-align: center; font-size: 12.8px; line-height: 19.6px; color: var(--blue-deep); }

  /* audience cards */
  .card { top: 478px; width: 336px; height: 198px; overflow: hidden; }
  .card-art { position: absolute; left: 0; top: 0; }
  .card-icon { left: 33px; top: 17px; }
  .card-title { left: 26px; top: 44px; font-size: 21px; font-weight: 300; color: var(--white); line-height: 26px; }
  .card-body { left: 26px; top: 74px; width: 150px; font-size: 9.5px; line-height: 17px; color: var(--white); }
  .card .btn { top: 139px; left: 27px; width: 116px; height: 29px; }
  .btn-blue { background: var(--blue); }
  .btn-dark { background: var(--charcoal); }

  .offer-title { left: 0; top: 702px; width: 1013px; text-align: center; font-size: 19px; font-weight: 300; color: var(--navy); line-height: 24px; }
  .offer-list { top: 734px; list-style: none; font-size: 9.6px; line-height: 17px; color: var(--text); }
  .offer-list li { display: flex; align-items: center; gap: 6px; }

  /* grey band */
  .band { left: 0; top: 814px; width: 1015px; height: 300px; background: var(--grey-band); }
  .section-title { top: 845px; font-size: 18px; font-weight: 300; color: var(--navy); line-height: 22px; }
  .quote { left: 171px; width: 310px; font-size: 9.6px; font-style: italic; line-height: 16.8px; color: var(--text); }
  .client { left: 171px; font-size: 8px; line-height: 12px; color: var(--text); }
  .client b { font-weight: 700; }
  .rule { top: 1055px; height: 1px; background: var(--rule); }
  .more { top: 1064px; font-size: 9.5px; font-weight: 500; color: var(--link); line-height: 12px; }

  .job-title { left: 516px; font-size: 11.5px; font-weight: 400; color: var(--navy); line-height: 14px; }
  .job-title.small { font-size: 9.8px; }
  .job-meta { left: 516px; font-size: 9.4px; color: var(--text); line-height: 12px; }
  .job-meta b { font-weight: 700; }
  .job-link { left: 516px; font-size: 9.4px; font-weight: 500; color: var(--link); line-height: 12px; }

  /* footer */
  .foot-nav { left: 0; top: 1114px; width: 1015px; height: 34px; background: var(--blue); }
  .foot-nav a { position: absolute; top: 0; line-height: 34px; font-size: 9px; font-weight: 700; color: var(--white); }
  .foot-nav span { position: absolute; top: 12px; width: 10px; height: 10px; border-radius: 50%; background: #0a7fbd; }
  .foot-base { left: 0; top: 1148px; width: 1015px; height: 52px; background: var(--charcoal); }
  .copyright { left: 171px; top: 1168px; font-size: 7px; color: #a9a9a9; }
</style>
</head>
<body>

<nav class="abs top-nav">
  <a href="#" style="left:170px">Home</a>
  <a href="#" style="left:264px">About Us</a>
  <a href="#" style="left:371px">What we do</a>
  <a href="#" style="left:586px">Employers</a>
  <a href="#" style="left:690px">Candidates</a>
  <a href="#" style="left:796px">Contact Us</a>
</nav>
<div class="abs brand-tab"></div>
<div class="abs brand-dot"></div>
<div class="abs brand">Brightvale</div>

<div class="social-top">
  <span style="left:167px"></span><span style="left:193px"></span><span style="left:221px"></span>
</div>
<div class="abs phone">
  <svg width="20" height="20" viewBox="0 0 20 20" aria-hidden="true">
    <circle cx="10" cy="10" r="9" fill="none" stroke="#c5c5c5" stroke-width="1.2"/>
    <path d="M7 5.5c-.8.4-1.5 1.3-1 3 .8 2.6 3 4.8 5.5 5.6 1.7.5 2.6-.2 3-1l-2-1.6-1.2.8c-1.3-.5-2.4-1.6-2.9-2.9l.8-1.2z" fill="#c5c5c5"/>
  </svg>
  <span>Call <b>01 555 0192</b></span>
</div>

<section class="abs hero">
  <svg class="hero-art" width="785" height="242" viewBox="0 0 981 303" preserveAspectRatio="none">
    <defs>
      <linearGradient id="teamPhoto" x1="0" y1="0" x2="0" y2="1">
        <stop offset="0" stop-color="#ecedef"/>
        <stop offset="0.55" stop-color="#9a9ba1"/>
        <stop offset="1" stop-color="#3d3c42"/>
      </linearGradient>
    </defs>
    <rect width="981" height="303" fill="url(#teamPhoto)" role="img" aria-label="Photo of the recruitment team standing together in business dress"/>
    <path d="M0 0H438C548 70 560 228 452 303H0Z" fill="#00aeef"/>
    <path d="M0 0H438C532 70 520 225 420 303H400C500 225 520 80 418 0Z" fill="#d8dade"/>
    <path d="M0 0H422C515 75 505 220 410 303H0Z" fill="#00aeef"/>
  </svg>
  <h1 class="abs hero-title">Welcome to Brightvale</h1>
  <p class="abs hero-sub">IT Recruitment Specialists</p>
  <a href="#" class="abs btn btn-hero">Find out more about what we do
    <svg width="16" height="12" viewBox="0 0 16 12" aria-hidden="true"><path d="M10 0l6 5.5-6 5.5V8C5 8 2 9 0 12 1 6 4 3.5 10 3z" fill="#fff"/></svg>
  </a>
</section>

<p class="abs intro">Lorem ipsum dolor sit amet, consectetur adipiscing elit, sed do eiusmod tempor incididunt ut labore et dolore magna aliqua enim ad minim veniam, quis nostrud exercitation ullamco laboris nisi ut aliquip ex ea commodo consequat aute irure dolor in reprehenderit in voluptate velit esse cillum dolore eu fugiat.</p>

<article class="abs card" style="left:173px">
  <svg class="card-art" width="336" height="198" viewBox="0 0 420 247" preserveAspectRatio="none">
    <defs>
      <linearGradient id="employerPhoto" x1="0" y1="0" x2="1" y2="1">
        <stop offset="0" stop-color="#8d9bb3"/>
        <stop offset="0.5" stop-color="#4f5560"/>
        <stop offset="1" stop-color="#2b2a2d"/>
      </linearGradient>
    </defs>
    <rect width="420" height="247" fill="url(#employerPhoto)" role="img" aria-label="Photo of an employer working at a laptop"/>
    <path d="M0 0H200C285 70 285 190 200 247H0Z" fill="#454344"/>
    <path d="M180 0H220C290 80 290 180 220 247H190C265 180 265 80 180 0Z" fill="#454344" opacity=".85"/>
  </svg>
  <svg class="abs card-icon" width="16" height="20" viewBox="0 0 16 20" aria-hidden="true"><circle cx="8" cy="5" r="4.5" fill="#00aeef"/><path d="M0 20v-4c0-3 3-5.5 8-5.5s8 2.5 8 5.5v4z" fill="#00aeef"/></svg>
  <h2 class="abs card-title">Employers</h2>
  <p class="abs card-body" style="width:142px">Lorem ipsum dolor sit amet odio consectetur adipiscing &nbsp;eiusmod incididunt dolore.</p>
  <a href="#" class="abs btn btn-blue">Find out more
    <svg width="13" height="10" viewBox="0 0 16 12" aria-hidden="true"><path d="M10 0l6 5.5-6 5.5V8C5 8 2 9 0 12 1 6 4 3.5 10 3z" fill="#fff"/></svg>
  </a>
</article>

<article class="abs card" style="left:510px">
  <svg class="card-art" width="336" height="198" viewBox="0 0 420 247" preserveAspectRatio="none">
    <defs>
      <linearGradient id="candidatePhoto" x1="0" y1="0" x2="1" y2="1">
        <stop offset="0" stop-color="#5d7a45"/>
        <stop offset="0.5" stop-color="#d9c2c0"/>
        <stop offset="1" stop-color="#f1eeee"/>
      </linearGradient>
    </defs>
    <rect width="420" height="247" fill="url(#candidatePhoto)" role="img" aria-label="Photo of a candidate on the phone at her desk"/>
    <path d="M170 0H215C295 80 290 190 205 247H175C265 185 265 75 170 0Z" fill="#00aeef"/>
    <path d="M0 0H185C260 75 255 190 180 247H0Z" fill="#00aeef"/>
  </svg>
  <svg class="abs card-icon" style="left:30px" width="24" height="20" viewBox="0 0 24 20" aria-hidden="true"><circle cx="7" cy="5" r="4.5" fill="#454344"/><circle cx="17" cy="7" r="3.6" fill="#454344"/><path d="M0 20v-4c0-3 3-5.5 7-5.5s7 2.5 7 5.5v4z" fill="#454344"/><path d="M15 20v-3c0-2-1-3.5-2-4.5 1-.8 2.5-1.2 4-1.2 4 0 7 2 7 4.5V20z" fill="#454344"/></svg>
  <h2 class="abs card-title">Candidates</h2>
  <p class="abs card-body" style="left:30px;width:130px">Enim ad minim veniam quis nostrud laboris nisi ut aliquip commodo adipiscing elit.</p>
  <a href="#" class="abs btn btn-dark" style="left:30px">Find out more
    <svg width="13" height="10" viewBox="0 0 16 12" aria-hidden="true"><path d="M10 0l6 5.5-6 5.5V8C5 8 2 9 0 12 1 6 4 3.5 10 3z" fill="#fff"/></svg>
  </a>
</article>

<h2 class="abs offer-title">We offer specialist recruitment knowledge and experience in ...</h2>
<ul class="abs offer-list" style="left:270px">
  <li><svg width="7" height="6" viewBox="0 0 16 12"><path d="M10 0l6 5.5-6 5.5V8C5 8 2 9 0 12 1 6 4 3.5 10 3z" fill="#00aeef"/></svg>Lorem ipsum dolor consectetur</li>
  <li><svg width="7" height="6" viewBox="0 0 16 12"><path d="M10 0l6 5.5-6 5.5V8C5 8 2 9 0 12 1 6 4 3.5 10 3z" fill="#00aeef"/></svg>Adipiscing elit sed eiusmod</li>
  <li><svg width="7" height="6" viewBox="0 0 16 12"><path d="M10 0l6 5.5-6 5.5V8C5 8 2 9 0 12 1 6 4 3.5 10 3z" fill="#00aeef"/></svg>Tempor incididunt labore</li>
</ul>
<ul class="abs offer-list" style="left:443px">
  <li><svg width="7" height="6" viewBox="0 0 16 12"><path d="M10 0l6 5.5-6 5.5V8C5 8 2 9 0 12 1 6 4 3.5 10 3z" fill="#00aeef"/></svg>Duisaute reprehenderit</li>
  <li><svg width="7" height="6" viewBox="0 0 16 12"><path d="M10 0l6 5.5-6 5.5V8C5 8 2 9 0 12 1 6 4 3.5 10 3z" fill="#00aeef"/></svg>Voluptate velit esse cillum</li>
  <li><svg width="7" height="6" viewBox="0 0 16 12"><path d="M10 0l6 5.5-6 5.5V8C5 8 2 9 0 12 1 6 4 3.5 10 3z" fill="#00aeef"/></svg>Excepteur sint occaecat</li>
</ul>
<ul class="abs offer-list" style="left:599px">
  <li><svg width="7" height="6" viewBox="0 0 16 12"><path d="M10 0l6 5.5-6 5.5V8C5 8 2 9 0 12 1 6 4 3.5 10 3z" fill="#00aeef"/></svg>Dolore magna aliquat enim</li>
  <li><svg width="7" height="6" viewBox="0 0 16 12"><path d="M10 0l6 5.5-6 5.5V8C5 8 2 9 0 12 1 6 4 3.5 10 3z" fill="#00aeef"/></svg>Veniam quis nostrud exercitation</li>
  <li><svg width="7" height="6" viewBox="0 0 16 12"><path d="M10 0l6 5.5-6 5.5V8C5 8 2 9 0 12 1 6 4 3.5 10 3z" fill="#00aeef"/></svg>Ullamco laboris</li>
</ul>

<div class="abs band"></div>

<h2 class="abs section-title" style="left:171px">What our clients think</h2>
<p class="abs quote" style="top:876px">“Culpa qui officia deserunt mollit anim id est laborum magna aliqua. Ut enim ad minim veniam, quis nostrud exercitation ullamco laboris nisi ut aliquip ex ea commodo consequat. Duis aute irure dolor in reprehenderit in voluptate velit.”</p>
<p class="abs client" style="top:946px"><b>Client Name</b> . Company</p>
<p class="abs quote" style="top:971px">“Duis aute irure dolor in reprehenderit in voluptate velit esse cillum dolore eu fugiat nulla pariatur. Excepteur sint occaecat cupidatat non proident, sunt in culpa qui officia deserunt mollit anim id est laborum.”</p>
<p class="abs client" style="top:1025px"><b>Client Name</b> . Company</p>
<div class="abs rule" style="left:171px;width:328px"></div>
<a href="#" class="abs more" style="left:173px">Read more testimonials ›</a>

<h2 class="abs section-title" style="left:516px">Latest Vacancies</h2>
<h3 class="abs job-title" style="top:879px">IT Support Analyst</h3>
<p class="abs job-meta" style="top:898px"><b>Salary:</b> €25,000 | <b>Type:</b> Permanent | <b>Location:</b> Location Name</p>
<a href="#" class="abs job-link" style="top:915px">Find out more ›</a>
<h3 class="abs job-title" style="top:937px">Java Developer</h3>
<p class="abs job-meta" style="top:955px"><b>Salary:</b> €28,000 | <b>Type:</b> Temporary - 3 months | <b>Location:</b> Location Name</p>
<a href="#" class="abs job-link" style="top:972px">Find out more ›</a>
<h3 class="abs job-title small" style="top:994px">IT Support Analyst</h3>
<p class="abs job-meta" style="top:1011px"><b>Salary:</b> €29,000 | <b>Type:</b> Permanent | <b>Location:</b> Location Name</p>
<a href="#" class="abs job-link" style="top:1028px">Find out more ›</a>
<div class="abs rule" style="left:516px;width:330px"></div>
<a href="#" class="abs more" style="left:516px">See more vacancies ›</a>

<footer>
  <nav class="abs foot-nav">
    <a href="#" style="left:170px">Home</a>
    <a href="#" style="left:234px">About Us</a>
    <a href="#" style="left:310px">What we do</a>
    <a href="#" style="left:396px">Employers</a>
    <a href="#" style="left:478px">Candidates</a>
    <a href="#" style="left:562px">Contact Us</a>
    <span style="left:780px"></span><span style="left:805px"></span><span style="left:833px"></span>
  </nav>
  <div class="abs foot-base"></div>
  <p class="abs copyright">© 2015 Brightvale Recruitment</p>
</footer>

</body>
</html>
```